The Hollow - Short Film Poster Design

A short film that follows a forest ranger contemplating suicide as he stumbles upon three kids lost in the forest, each in their own, different way.

Genre: Contemporary Dark Drama

Seeking a poster that really stands out as a 'Festival Piece'. See the following lists for references:

QRVN Festival Poster Awards: https://www.snapvault.example/photos/officialqrvn/with/48203917562/

Here is the FULL RESOLUTION short film to take screen grabs and reference photos from:
https://www.filecrate.example/s/kp7wq2rzt91mxe4/Hollow014.mov?oref=e

We are open to much of anything, but this project needs to stand out as unique. On top of that, we are trying to push the angle of strangers LOST in the forest (hence the name) and have thought of the opening sequence of the young man walking through the woods on the epic wide shot of being used for the poster art.

Various items need to be included on the poster: (Please feel free to reword as appropriate)

1) A FILM BY GORDON FAIRWEATHER
2) A DENNIS HOLMGRAVE PRODUCTION

All other taglines are optional and subject to addition or removal.

Please message with all other questions and comments.
Updates

Hey everyone, I apologize for not providing a high enough resolution copy of the short. I was told that this was the highest resolution until I got back straight from my editor who said it's a preliminary. Unfortunately, I do not have the ENTIRE film at top resolution. I will, however, attach high resolution .tiffs from various points of the film for use. https://www.filecrate.example/sh/wte8pqz41nd75ub/BBXKTmcPoLRWqDYe27fhZwNtb?dl=0

Industry/Entity Type

Film Production

Font styles to use
Serif
Sans Serif

Requirements
Must have
• 1) A FILM BY GORDON FAIRWEATHER
• 2) A DENNIS HOLMGRAVE PRODUCTION
• "THE HOLLOW" - Name of Film
Nice to have
• Tagline, but not necessary.

```html
<!DOCTYPE html>
<html lang="en">
<head>
<meta charset="utf-8">
<title>The Hollow — Short Film Poster</title>
<link rel="stylesheet" href="https://fonts.googleapis.com/css2?family=Oswald:wght@200;300;400&display=swap">
<style>
  :root {
    --page: #ffffff;
    --forest-dark: #2b2926;
    --forest-mid: #5a554e;
    --forest-light: #8a847a;
    --title-red: #c8202a;
    --credit-white: #eeeae4;
  }
  * { margin: 0; padding: 0; box-sizing: border-box; }
  html, body {
    width: 1200px;
    height: 1200px;
    overflow: hidden;
    background: var(--page);
  }
  .canvas {
    position: relative;
    width: 1200px;
    height: 1200px;
    background: var(--page);
  }
  .poster {
    position: absolute;
    left: 305px;
    top: 161px;
    width: 590px;
    height: 876px;
    overflow: hidden;
    font-family: "Oswald", "Arial Narrow", sans-serif;
  }
  .poster-art {
    position: absolute;
    inset: 0;
    background:
      linear-gradient(90deg,
        var(--forest-dark) 0%, var(--forest-mid) 8%, var(--forest-dark) 14%,
        var(--forest-light) 22%, var(--forest-mid) 30%, var(--forest-dark) 38%,
        var(--forest-mid) 48%, var(--forest-light) 56%, var(--forest-mid) 64%,
        var(--forest-dark) 74%, var(--forest-mid) 84%, var(--forest-dark) 100%);
  }
  .poster-art::after {
    content: "";
    position: absolute;
    inset: 0;
    background: linear-gradient(180deg, rgba(30,28,25,0.25) 0%, rgba(30,28,25,0) 40%, rgba(30,28,25,0.35) 100%);
  }
  .film-title {
    position: absolute;
    left: 0;
    right: 0;
    top: 350px;
    text-align: center;
    color: var(--title-red);
    font-weight: 300;
    font-size: 122px;
    line-height: 1;
    letter-spacing: 2px;
    transform: scaleY(1.18);
  }
  .credits {
    position: absolute;
    left: 0;
    right: 0;
    top: 700px;
    text-align: center;
    color: var(--credit-white);
  }
  .credit-director {
    font-weight: 300;
    font-size: 21px;
    letter-spacing: 2px;
    line-height: 1.3;
  }
  .credit-producer {
    font-weight: 300;
    font-size: 13px;
    letter-spacing: 1.5px;
    line-height: 1.4;
  }
</style>
</head>
<body>
  <main class="canvas">
    <article class="poster">
      <div class="poster-art" role="img" aria-label="Motion-blurred black and white photograph of a dense forest of thin tree trunks"></div>
      <h1 class="film-title">THE HOLLOW</h1>
      <div class="credits">
        <p class="credit-director">A FILM BY GORDON FAIRWEATHER</p>
        <p class="credit-producer">A DENNIS HOLMGRAVE PRODUCTION</p>
      </div>
    </article>
  </main>
</body>
</html>
```